Birthday Party Invitation

I need to create a "save the date" for my birthday party.
Text:

Save the Date
Saturday, 6 December 2014
9 pm
Club la Brisa, Lindenweg 42, 8005 Zürich
BLACK IT OUT
SAVE IT!
RESERVE THE TIME
WRITE IT DOWN
HOLD THE DATE to LET YOUR HAIR DOWN and Party with Me.

Target Market(s)

Friends

Industry/Entity Type

Club

Requirements
Must have
• I want the flyer to look classy and sexy at the same time.
Nice to have
• Picture on the left or right, then text white on black background. Maybe a simple frame. Not too playful, rather simple, elegant and no graphics. Just picture and text.

```html
<!DOCTYPE html>
<html lang="en">
<head>
<meta charset="utf-8">
<title>Save the Date – Birthday Party</title>
<link href="https://fonts.googleapis.com/css2?family=Josefin+Sans:wght@300;400&family=Oswald:wght@300&display=swap" rel="stylesheet">
<style>
  :root {
    --backdrop: #e6e6e6;
    --card-black: #050505;
    --white: #ffffff;
    --gold: #e2b47c;
    --pink: #f0787a;
    --rule-pink: #e86a6c;
    --rule-grey: #9a9a9a;
    --photo-dark: #1c0f09;
    --photo-warm: #4a2414;
  }
  * { margin: 0; padding: 0; box-sizing: border-box; }
  html, body {
    width: 1200px; height: 900px; overflow: hidden;
    background: var(--backdrop);
  }
  .stage {
    width: 1200px; height: 900px;
    display: flex; align-items: center; justify-content: center;
  }
  .invitation {
    width: 340px; height: 840px;
    background: var(--card-black);
    display: flex; flex-direction: column;
    box-shadow: 0 6px 24px rgba(0,0,0,0.25);
  }
  .invitation__text {
    padding: 22px 24px 16px 26px;
    color: var(--white);
  }
  .headline {
    font-family: "Josefin Sans", sans-serif;
    font-weight: 300;
    text-transform: uppercase;
    line-height: 0.88;
  }
  .headline__word {
    display: block;
    font-size: 100px;
    letter-spacing: 2px;
  }
  .headline__word--save { margin-left: -4px; }
  .headline__word--date { text-align: right; margin-right: -4px; }
  .headline__joiner {
    display: flex; align-items: center; justify-content: center;
    gap: 10px;
    font-size: 18px; letter-spacing: 2px;
    color: var(--white);
    margin: 2px 0 0;
  }
  .headline__joiner::before,
  .headline__joiner::after {
    content: ""; width: 58px; height: 3px; background: var(--rule-pink);
  }
  .details {
    margin-top: 14px;
    font-family: "Oswald", sans-serif;
    font-weight: 300;
  }
  .details__date, .details__address {
    color: var(--gold); font-size: 20px; line-height: 1.25;
  }
  .details__venue {
    font-family: "Josefin Sans", sans-serif;
    font-weight: 300; text-transform: uppercase;
    font-size: 23px; letter-spacing: 1px; line-height: 1.2;
    color: var(--white);
  }
  .mantra {
    margin-top: 12px;
    font-family: "Josefin Sans", sans-serif;
    font-weight: 300; text-transform: uppercase;
    color: var(--pink);
    font-size: 16px; line-height: 1.12;
    text-align: center;
  }
  .mantra__lead { font-size: 19px; display: block; }
  .ampersand {
    display: block; text-align: center;
    color: var(--white); font-family: "Josefin Sans", sans-serif;
    font-size: 12px; margin-top: 2px;
  }
  .closing {
    border-top: 1px solid var(--rule-grey);
    margin-top: 4px;
    padding-top: 10px;
    font-family: "Josefin Sans", sans-serif;
    font-weight: 300; text-transform: uppercase;
    font-size: 23px; letter-spacing: 2px;
    color: var(--white);
  }
  .invitation__photo {
    flex: 1;
    background: linear-gradient(170deg, var(--photo-dark) 0%, var(--photo-warm) 50%, var(--photo-dark) 100%);
  }
</style>
</head>
<body>
  <main class="stage">
    <article class="invitation">
      <section class="invitation__text">
        <h1 class="headline">
          <span class="headline__word headline__word--save">Save</span>
          <span class="headline__joiner">the</span>
          <span class="headline__word headline__word--date">Date</span>
        </h1>
        <div class="details">
          <p class="details__date">Saturday, 6 December 2014, 9 pm</p>
          <p class="details__venue">Club la Brisa</p>
          <p class="details__address">Lindenweg 42, 8005 Zürich</p>
        </div>
        <p class="mantra">
          <span class="mantra__lead">Black it out! Save it!</span>
          Reserve the time, write it down, hold the date to let your hair down
        </p>
        <span class="ampersand">&amp;</span>
        <p class="closing">Party with me</p>
      </section>
      <div class="invitation__photo" role="img" aria-label="Photo of the host in a festive red outfit against a dark warm background"></div>
    </article>
  </main>
</body>
</html>
```